Bold Cover needed for a book on Workplace Bullying

I need a book cover design for a book titled, “Iron Silence?” The book recounts my story of bullying in the workplace. It also includes chapters on how readers can minimize/stop workplace bullying, write an effective complaint, and ensure their own mental wellbeing.
I am looking for a bold design using red and black, and possibly distressed lettering. The covers of other books dealing with this subject do not reflect my vision. They are often too childish or look too academic. This book needs to stress the serious nature of a toxic workplace, while appealing to readers experiencing a similar situation. I’d like the cover to reflect the mental anguish associated with workplace bullying (hence the distressed lettering).
I have included a cover that appeals to me (although the coloring is wrong). That said, I am also very happy (and excited) to see your creative input!
On the cover, it should have the following:
Title: Iron Silence?
Subtitle: How the Harbour Works Department Condones Bullying & Ruins Lives
Author: Owen Frick
Other relevant details:
Book size: 5.5” x 8.5”
Back cover will have a blurb, author picture/short bio, and barcode
The blurb on the back cover reads:
Undermining, intimidation and threats
Despite the Department of Harbour Works allegedly holding a zero tolerance for bullying, these behaviours were an everyday occurrence in at least one workplace. Even after a decade of complaints, numerous witnesses and physical proof, the department failed to act. Instead, they looked the other way, allowing one powerful and well-connected individual to end careers and ruin lives.
After being targeted, one teacher resolved to put an end to the abuse experienced by more than fifty employees. His startling story reveals the relentless bullying, mental health ramifications, and insidious tactics used to cover up the corrosive behaviour.
Those who have experienced a toxic workplace will also find much needed support and guidance, intended to minimise suffering and detail a clear way forward. Chapters include dealing with bullying in the workplace, how to lodge a successful complaint, and how to stay sane during any potential legal action.

```html
<!DOCTYPE html>
<html lang="en">
<head>
<meta charset="utf-8">
<title>Iron Silence? — Book Cover</title>
<link rel="stylesheet" href="https://fonts.googleapis.com/css2?family=Rubik+Dirt&family=Arvo:wght@400;700&display=swap">
<style>
  :root {
    --backdrop: #acacac;
    --ink: #000000;
    --red: #cc0000;
    --red-shade: #a30000;
    --red-deep: #7a0000;
  }
  html, body {
    margin: 0;
    padding: 0;
    width: 1200px;
    height: 1200px;
    overflow: hidden;
    background: var(--backdrop);
  }
  .canvas {
    position: relative;
    width: 1200px;
    height: 1200px;
  }
  .cover {
    position: absolute;
    left: 259px;
    top: 70px;
    width: 679px;
    height: 1050px;
    overflow: hidden;
    background: var(--red);
  }
  .cover-art {
    position: absolute;
    inset: 0;
    width: 100%;
    height: 100%;
  }
  .title-word {
    font-family: "Rubik Dirt", "Arial Black", sans-serif;
    letter-spacing: 2px;
  }
  .subtitle {
    position: absolute;
    left: 190px;
    width: 460px;
    top: 946px;
    margin: 0;
    text-align: center;
    font-family: "Arvo", "Rockwell", serif;
    font-weight: 400;
    font-size: 20px;
    line-height: 27px;
    color: var(--ink);
  }
  .author {
    position: absolute;
    left: 190px;
    width: 460px;
    top: 1012px;
    margin: 0;
    text-align: center;
    font-family: "Arvo", "Rockwell", serif;
    font-weight: 700;
    font-size: 21px;
    letter-spacing: 0.5px;
    color: var(--ink);
  }
</style>
</head>
<body>
<main class="canvas">
  <section class="cover">
    <svg class="cover-art" viewBox="0 0 679 1050" xmlns="http://www.w3.org/2000/svg">
      <!-- diagonal split -->
      <polygon class="dark-field" points="0,0 679,0 0,1050" fill="var(--ink)"/>

      <!-- decorative grin icons -->
      <circle cx="138" cy="163" r="87" fill="var(--red-deep)" role="img" aria-label="Large laughing emoji illustration in red line"/>
      <circle cx="325" cy="182" r="34" fill="var(--red-deep)" role="img" aria-label="Small sneering emoji illustration"/>
      <circle cx="86" cy="461" r="36" fill="var(--red-deep)" role="img" aria-label="Small smirking emoji illustration"/>

      <!-- worried icons and distressed figure -->
      <circle cx="508" cy="530" r="14" fill="var(--red-shade)" role="img" aria-label="Tiny upset emoji illustration"/>
      <circle cx="579" cy="537" r="14" fill="var(--red-shade)" role="img" aria-label="Tiny upset emoji illustration"/>
      <rect x="446" y="562" width="230" height="350" rx="40" fill="var(--red-shade)" role="img" aria-label="Sketch of a distressed person covering their head, standing in a dark shadow"/>

      <!-- title -->
      <text class="title-word" transform="translate(232 520) rotate(-57)" text-anchor="middle"
            font-size="150" fill="var(--red)">IRON</text>
      <text class="title-word" transform="translate(378 612) rotate(-57)" text-anchor="middle"
            font-size="128" fill="var(--ink)">SILENCE?</text>
    </svg>

    <p class="subtitle">"How the Harbour Works Department<br>Condones Bullying &amp; Ruins Lives"</p>
    <p class="author">OWEN FRICK</p>
  </section>
</main>
</body>
</html>
```